All Natural Mosquito Repellent

My company, BrightFern Company has created an all natural mosquito repellent. I already have other all natural products that I have developed and created labels for. I will include a copy of that label so you have something to work from. I will need two labels. One for the front of the bottle and one for the back. The back label will need space for a UPC. The labels need to be 63mm (H) x 39mm (W)

Target Market(s)

Consumers, Organic, People who like natural products

Font styles to use
Other font styles liked:
• A combination of both Serif and Sans Serif

Requirements
Must have
• Use the words Organic, All Natural, Travel size, made in the USA label
Nice to have
• tag line: Don't beat them off. Spray them away.

```html
<!DOCTYPE html>
<html lang="en">
<head>
<meta charset="utf-8">
<title>BrightFern Company – Fern Mosquito Repellent Labels</title>
<link href="https://fonts.googleapis.com/css2?family=Carlito:wght@400;700&family=Oswald:wght@500;600&family=Noto+Serif:wght@400&family=Dancing+Script:wght@500&family=Roboto+Slab:wght@800&display=swap" rel="stylesheet">
<style>
  :root{
    --backdrop:#666666;
    --label:#ffffff;
    --orange:#f26a06;
    --ink:#1a1a1a;
    --grey:#444444;
    --red:#e31e24;
  }
  *{box-sizing:border-box;margin:0;padding:0}
  html,body{width:1200px;height:1200px;overflow:hidden}
  body{background:var(--backdrop);position:relative;font-family:'Carlito',sans-serif;color:var(--ink)}
  .label{position:absolute;top:358px;width:300px;height:485px;background:var(--label);border-radius:8px;overflow:hidden}
  .label--front{left:210px}
  .label--back{left:690px}

  /* front */
  .brand{position:absolute;top:28px;left:0;width:100%;text-align:center}
  .brand__mark{display:inline-flex;align-items:center;gap:8px}
  .brand__dot{width:34px;height:34px;border-radius:50%;background:var(--orange)}
  .brand__name{font-family:'Carlito',sans-serif;font-size:19px;letter-spacing:1px;color:var(--grey)}
  .brand__note{font-size:6px;color:var(--grey);margin-top:4px;word-spacing:2px}
  .product{position:absolute;top:128px;width:100%;text-align:center}
  .product__line{font-family:'Carlito',sans-serif;font-size:19px;color:var(--ink)}
  .product__name{font-family:'Oswald',sans-serif;font-weight:600;font-size:25px;color:var(--orange);line-height:1.05;letter-spacing:.2px}
  .product__tagline{font-family:'Noto Serif',serif;font-size:16px;line-height:1.25;margin-top:8px;color:var(--ink)}
  .product__promise{font-family:'Dancing Script',cursive;font-size:13px;color:var(--orange);margin-top:10px}
  .claims{position:absolute;left:22px;top:344px;list-style:none;font-family:'Oswald',sans-serif;font-weight:500;font-size:10.5px;line-height:1.4;color:var(--ink)}
  .claims li::before{content:"•";color:var(--orange);margin-right:4px}
  .icon-area{position:absolute;left:98px;top:300px;width:112px;height:112px;border-radius:50%;background:radial-gradient(circle,#e9e9e9 0%,#cfcfcf 100%);border:9px solid var(--red)}
  .net{position:absolute;right:18px;top:356px;text-align:right;font-family:'Oswald',sans-serif;font-weight:500;font-size:10.5px;line-height:1.3}
  .origin{position:absolute;left:0;bottom:0;width:100%;height:64px}
  .origin__text{position:absolute;left:0;bottom:7px;width:100%;text-align:center;font-family:'Roboto Slab',serif;font-weight:800;font-size:15px;line-height:1.1;color:#fff}
  .origin__text span{font-size:9px;vertical-align:middle;margin:0 6px}

  /* back */
  .section{text-align:center;margin-top:12px}
  .section:first-child{margin-top:28px}
  .section__title{display:inline-block;background:var(--orange);color:#fff;font-weight:700;font-size:10px;padding:3px 6px}
  .section__body{font-size:6.3px;line-height:1.45;color:var(--ink);margin:8px 22px 0}
  .address{margin:28px 0 0 68px;width:160px}
  .address__title{font-size:11.5px;font-weight:700;text-align:center;margin-bottom:6px}
  .address__body{font-size:8.5px;line-height:1.35}
  .recycle{position:absolute;left:16px;bottom:38px;width:40px;height:40px}
  .upc{position:absolute;left:74px;bottom:26px;width:190px;height:56px;border:2px solid var(--ink);display:flex;align-items:center;justify-content:center;font-size:20px}
</style>
</head>
<body>

<section class="label label--front">
  <div class="brand">
    <div class="brand__mark"><span class="brand__dot"></span><span class="brand__name">BRIGHTFERN CO.</span></div>
    <p class="brand__note">crafted by hand, with love &nbsp;&nbsp; in the U.S.A.</p>
  </div>
  <div class="product">
    <p class="product__line">FERN</p>
    <h1 class="product__name">MOSQUITO REPELLENT</h1>
    <p class="product__tagline">“Don't beat them off<br>Spray them away”</p>
    <p class="product__promise">long lasting protection</p>
  </div>
  <ul class="claims">
    <li>ORGANIC</li>
    <li>ALL NATURAL</li>
    <li>TRAVEL SIZE</li>
  </ul>
  <div class="icon-area" role="img" aria-label="No-mosquito symbol: mosquito illustration crossed out in a red prohibition circle"></div>
  <p class="net">NET WEIGHT<br>50 ML</p>
  <div class="origin">
    <svg width="300" height="64" viewBox="0 0 300 64" aria-hidden="true"><path d="M0 26 Q150 -14 300 26 L300 64 L0 64 Z" fill="var(--orange)"/></svg>
    <p class="origin__text"><span>★</span>Made in<span>★</span><br>the USA</p>
  </div>
</section>

<section class="label label--back">
  <div class="section">
    <h2 class="section__title">DIRECTION FOR USE:</h2>
    <p class="section__body">There are many variations of passages of Lorem Ipsum available, but the majority have suffered alteration in some form, by injected humour, or randomised words which don't look even slightly believable. If you are going to use a passage of Lorem Ipsum, you need to be sure there isn't anything embarrassing hidden in the middle of text.</p>
  </div>
  <div class="section">
    <h2 class="section__title">PRECAUTION:</h2>
    <p class="section__body">There are many variations of passages of Lorem Ipsum available, but the majority have suffered alteration in some form, by injected humour, or randomised words which don't look even slightly believable.</p>
  </div>
  <div class="section">
    <h2 class="section__title">INGREDIENTS:</h2>
    <p class="section__body">There are many variations of passages of Lorem Ipsum available, but the majority have suffered alteration in some form, by injected humour, or randomised words which don't look even slightly believable.</p>
  </div>
  <div class="section">
    <h2 class="section__title">STORAGE:</h2>
    <p class="section__body">Store in a cool and dry place. Place empty container in<br>trash or recycle.</p>
  </div>
  <div class="address">
    <h3 class="address__title">Company Address:</h3>
    <p class="address__body">Lorem Ipsum is simply dummy text of the printing and typesetting industry.</p>
  </div>
  <svg class="recycle" viewBox="0 0 40 40" aria-label="Recycle" role="img">
    <g fill="none" stroke="var(--ink)" stroke-width="4.5" stroke-linejoin="round">
      <path d="M14 14 L20 4 L26 14"/>
      <path d="M31 20 L36 30 L25 30"/>
      <path d="M15 34 L4 34 L9 24"/>
    </g>
    <g fill="var(--ink)">
      <path d="M26 8 L32 12 L27 17 Z"/>
      <path d="M21 26 L25 35 L17 31 Z"/>
      <path d="M6 19 L13 17 L12 25 Z"/>
    </g>
  </svg>
  <div class="upc">UPC</div>
</section>

</body>
</html>
```